Brivond Technologies business card design

We need a business card designed with our new logo. it would be great if the card could communicate it is a technology based company.

Target Market(s)

system integrators

Industry/Entity Type

technology, IOT

Contact Information for Business Card

Name, designation, Address, telephone number, email address

Requirements
Must have
• logo and company name
Nice to have
• something to do with technology

```html
<!DOCTYPE html>
<html lang="en">
<head>
<meta charset="utf-8">
<title>Brivond Technologies business card</title>
<link rel="stylesheet" href="https://fonts.googleapis.com/css2?family=Lato:wght@400;700;900&display=swap">
<style>
  :root {
    --orange: #f7941d;
    --charcoal: #3b3a3b;
    --rule: #8a8a8a;
    --paper: #ffffff;
    --text: #333333;
  }
  * { margin: 0; padding: 0; box-sizing: border-box; }
  html, body {
    width: 1200px; height: 376px; overflow: hidden;
    background: var(--paper);
    font-family: "Lato", Arial, sans-serif;
    color: var(--text);
  }
  .sheet { position: relative; width: 1200px; height: 376px; }
  .card { position: absolute; top: 0; height: 376px; background: var(--paper); }
  .card--front { left: 0; width: 585px; }
  .card--back { left: 605px; width: 571px; }

  .bar { position: absolute; }
  .bar--orange { background: var(--orange); }
  .bar--dark { background: var(--charcoal); }

  .corner-accent {
    position: absolute; width: 56px; height: 56px;
    background: linear-gradient(135deg, var(--orange) 0%, #c9873a 55%, var(--charcoal) 100%);
    opacity: 0.85;
  }

  .brand { position: absolute; color: var(--charcoal); font-weight: 900; text-align: center; line-height: 1; }
  .brand__mark { display: block; background: var(--orange); margin: 0 auto; }
  .brand__name { display: block; text-transform: uppercase; }
  .brand--front { left: 0; top: 140px; width: 156px; }
  .brand--front .brand__mark { width: 30px; height: 30px; margin-bottom: 14px; }
  .brand--front .brand__name { font-size: 26px; letter-spacing: 1px; }
  .brand--front .brand__sub { font-size: 11px; letter-spacing: 2.4px; margin-top: 6px; }
  .brand--back { left: 185px; top: 118px; width: 200px; }
  .brand--back .brand__mark { width: 40px; height: 40px; margin-bottom: 36px; }
  .brand--back .brand__name { font-size: 36px; letter-spacing: 1px; }
  .brand--back .brand__sub { font-size: 14px; letter-spacing: 3.6px; margin-top: 9px; }

  .person { position: absolute; left: 205px; top: 118px; width: 361px; }
  .person__name { font-size: 22px; font-weight: 900; letter-spacing: 2px; color: var(--charcoal); line-height: 1.1; }
  .person__role { font-size: 13px; font-weight: 700; letter-spacing: 0.6px; color: var(--orange); margin-top: 7px; }
  .person__rule { height: 2px; background: var(--rule); margin-top: 13px; }
  .person__address { font-size: 11px; line-height: 16px; margin-top: 12px; }
  .contacts { display: flex; margin-top: 17px; font-size: 11px; }
  .contact { display: flex; align-items: center; gap: 4px; }
  .contact--phone { width: 139px; }
  .contact svg { width: 16px; height: 14px; fill: var(--charcoal); }
</style>
</head>
<body>
<div class="sheet">
  <section class="card card--front">
    <div class="bar bar--orange" style="left:65px; top:0; width:25px; height:113px;"></div>
    <div class="bar bar--dark" style="left:65px; top:252px; width:25px; height:116px;"></div>

    <div class="brand brand--front">
      <span class="brand__mark"></span>
      <span class="brand__name">Brivond</span>
      <span class="brand__name brand__sub">Technologies</span>
    </div>

    <div class="person">
      <h1 class="person__name">YOUR NAME</h1>
      <p class="person__role">Designation</p>
      <div class="person__rule"></div>
      <p class="person__address">Your address Lorem ipsum dolor sit amet,<br>consectetur adipiscing elit</p>
      <div class="contacts">
        <span class="contact contact--phone">
          <svg viewBox="0 0 16 14" aria-hidden="true"><path d="M1 4c0-2 3-3 7-3s7 1 7 3v1h-4V3.5H5V5H1zM3 6h10l2 7H1zM6 8h4v3H6z"/></svg>
          +0123456789
        </span>
        <span class="contact contact--mail">
          <svg viewBox="0 0 16 14" aria-hidden="true"><path d="M1 1l14 5-6 2-2 5z"/></svg>
          abc@mail.com
        </span>
      </div>
    </div>

    <div class="corner-accent" role="img" aria-label="Decorative pixel square pattern" style="left:502px; top:10px;"></div>
    <div class="corner-accent" role="img" aria-label="Decorative pixel square pattern" style="left:502px; top:304px;"></div>
  </section>

  <section class="card card--back">
    <div class="bar bar--orange" style="left:1px; top:174px; width:177px; height:23px;"></div>
    <div class="bar bar--dark" style="left:392px; top:174px; width:179px; height:23px;"></div>

    <div class="brand brand--back">
      <span class="brand__mark"></span>
      <span class="brand__name">Brivond</span>
      <span class="brand__name brand__sub">Technologies</span>
    </div>

    <div class="corner-accent" role="img" aria-label="Decorative pixel square pattern" style="left:10px; top:10px;"></div>
    <div class="corner-accent" role="img" aria-label="Decorative pixel square pattern" style="left:10px; top:304px;"></div>
    <div class="corner-accent" role="img" aria-label="Decorative pixel square pattern" style="left:504px; top:10px;"></div>
    <div class="corner-accent" role="img" aria-label="Decorative pixel square pattern" style="left:504px; top:304px;"></div>
  </section>
</div>
</body>
</html>
```